Fix our Takeaway Burger Box Graphics

We need the Graphics for our new Takeaway Burger Boxes fixed. Our in house Graphics Team had a go at these, but management don't like them. I have attached these for you to use as a guide. We do like the use of the Burger pattern, but believe it isn't placed well on the box.

We have 2 sizes. Small and Medium. Each design has to be different.

At the top of each box, you will notice a list of Burger Names with a Check Box next them. There are 7 Burger Names on the Small Box and 4 Burger Names on the Medium Box. This is so the staff can tick which burger is in the box.

I have attached our Company logo too which would be good to have on the box. Our slogan is Griddle, Sizzle, Juicy Patty Giver. This doesn't have to be on the box, but it can if it suits your design.

I have also attached the die cut/template.

The boxes will be made from brown/kraft cardboard. I attached a screen shot of what a Burger Clam/Box is in case you are not sure.

I have also attached an example of the packaging designs without our business so you can get an idea for fonts ect. And 2 examples of boxes that I like.

Many thanks, Mirela

Target Market(s)

Middle Income Families looking for something a bit fun and modern

Industry/Entity Type

Burger Restaurant

Requirements
Must have
• 2 Designs (Small and Medium). Each design top of lid must be different.
• List of Burgers that will be going into each size with a tick box next to them.
• Max 1 - 2 colours. White and Black look good on the kraft paper. Would be okay to put silver or gold as a secondary colour.
Nice to have
• Copperfield Grill Logo
• Griddle, Sizzle, Juicy Patty Giver Logo

```html
<!DOCTYPE html>
<html lang="en">
<head>
<meta charset="utf-8">
<title>Copperfield Grill – Takeaway Burger Box Dielines</title>
<link rel="stylesheet" href="https://fonts.googleapis.com/css2?family=Oswald:wght@400;600&display=swap">
<style>
  :root {
    --kraft: #e4b48f;
    --ink: #1b2225;
    --paper: #ffffff;
    --cut: #1b2225;
  }
  html, body {
    margin: 0;
    padding: 0;
    width: 1200px;
    height: 1144px;
    overflow: hidden;
    background: var(--paper);
  }
  .dieline-sheet { display: block; width: 1200px; height: 1144px; }
  .kraft { fill: var(--kraft); stroke: var(--cut); stroke-width: 1.2; }
  .ink { fill: var(--ink); stroke: var(--cut); stroke-width: 1.2; }
  .band-kraft { fill: var(--kraft); }
  .band-ink { fill: var(--ink); }
  .menu-item { font-family: "Oswald", sans-serif; font-weight: 400; font-size: 13px; letter-spacing: 0.5px; }
  .menu-item.on-ink { fill: var(--kraft); }
  .tick-box { fill: none; stroke-width: 1.6; }
  .tick-box.on-ink { stroke: var(--kraft); }
  .slogan { font-family: "Oswald", sans-serif; font-weight: 600; letter-spacing: 1px; }
  .slogan.small-box { fill: var(--kraft); font-size: 40px; }
  .slogan.medium-box { fill: var(--ink); font-size: 58px; }
  .brand-name { font-family: "Oswald", sans-serif; font-weight: 600; font-size: 24px; letter-spacing: 1px; text-anchor: middle; }
  .brand-name.on-ink { fill: var(--kraft); }
  .brand-name.on-kraft { fill: var(--ink); }
  .art-fill { fill: var(--ink); }
</style>
</head>
<body>
<svg class="dieline-sheet" viewBox="0 0 1580 1512" preserveAspectRatio="none" xmlns="http://www.w3.org/2000/svg">

  <!-- ========== SMALL BOX ========== -->
  <g class="small-box-dieline">
    <!-- lid top tuck -->
    <polygon class="ink" points="200,107 582,107 568,122 560,308 220,308 213,122"/>
    <path class="kraft" d="M213,175 L115,155 Q88,195 94,245 Q100,288 132,296 L220,308 Z"/>
    <path class="kraft" d="M567,175 L665,155 Q692,195 686,245 Q680,288 648,296 L560,308 Z"/>

    <!-- lid face with side flaps -->
    <path class="ink" d="M220,308 L68,286 Q58,286 59,300 L66,655 Q68,668 80,668 L120,680 L220,650 Z"/>
    <path class="ink" d="M560,308 L712,286 Q722,286 721,300 L714,655 Q712,668 700,668 L660,680 L560,650 Z"/>
    <rect class="ink" x="220" y="308" width="340" height="342"/>
    <rect class="band-kraft" x="220" y="310" width="128" height="338"/>

    <!-- stripes -->
    <g class="band-kraft">
      <rect x="60" y="336" width="160" height="5"/><rect x="60" y="354" width="160" height="5"/>
      <rect x="348" y="336" width="372" height="5"/><rect x="348" y="354" width="372" height="5"/>
      <rect x="66" y="596" width="154" height="5"/><rect x="66" y="614" width="154" height="5"/>
      <rect x="348" y="596" width="366" height="5"/><rect x="348" y="614" width="366" height="5"/>
    </g>
    <g class="band-ink">
      <rect x="220" y="336" width="128" height="5"/><rect x="220" y="354" width="128" height="5"/>
      <rect x="220" y="596" width="128" height="5"/><rect x="220" y="614" width="128" height="5"/>
    </g>

    <rect class="art-fill" x="230" y="395" width="118" height="170" rx="40" role="img" aria-label="Burger pattern illustration"/>

    <!-- burger checklist -->
    <g class="burger-checklist">
      <g transform="translate(196,398) rotate(90)"><text class="menu-item on-ink">CHEESEY BURGER</text></g>
      <g transform="translate(176,398) rotate(90)"><text class="menu-item on-ink">KIWI DOUBLE DELUXE</text></g>
      <g transform="translate(156,398) rotate(90)"><text class="menu-item on-ink">CLASSIC FISH</text></g>
      <g transform="translate(136,398) rotate(90)"><text class="menu-item on-ink">NEW YORK OX</text></g>
      <g transform="translate(116,398) rotate(90)"><text class="menu-item on-ink">PORK N PINEAPPLE BURGER</text></g>
      <g transform="translate(96,398) rotate(90)"><text class="menu-item on-ink">DOUBLE CHEESEY BURGER</text></g>
      <g transform="translate(76,398) rotate(90)"><text class="menu-item on-ink">SPECIAL</text></g>
      <rect class="tick-box on-ink" x="196" y="378" width="10" height="10" rx="2"/>
      <rect class="tick-box on-ink" x="176" y="378" width="10" height="10" rx="2"/>
      <rect class="tick-box on-ink" x="156" y="378" width="10" height="10" rx="2"/>
      <rect class="tick-box on-ink" x="136" y="378" width="10" height="10" rx="2"/>
      <rect class="tick-box on-ink" x="116" y="378" width="10" height="10" rx="2"/>
      <rect class="tick-box on-ink" x="96" y="378" width="10" height="10" rx="2"/>
      <rect class="tick-box on-ink" x="76" y="378" width="10" height="10" rx="2"/>
    </g>

    <!-- slogan -->
    <g transform="rotate(180 470 485)">
      <text class="slogan small-box" x="400" y="425">GRIDDLE,</text>
      <text class="slogan small-box" x="400" y="465">SIZZLE,</text>
      <text class="slogan small-box" x="400" y="503">JUICY</text>
      <text class="slogan small-box" x="400" y="542">PATTY</text>
      <text class="slogan small-box" x="400" y="580">GIVER</text>
    </g>

    <!-- brand name on tuck -->
    <g transform="rotate(180 390 210)">
      <text class="brand-name on-ink" x="390" y="204">COPPERFIELD</text>
      <text class="brand-name on-ink" x="390" y="232">GRILL</text>
    </g>

    <!-- back and base -->
    <polygon class="ink" points="215,650 565,650 573,795 207,795"/>
    <polygon class="kraft" points="215,652 120,730 207,792"/>
    <polygon class="kraft" points="565,652 660,730 573,792"/>
    <polygon class="kraft" points="207,795 573,795 565,935 215,935"/>
    <polygon class="kraft" points="207,797 120,853 215,933"/>
    <polygon class="kraft" points="573,797 660,853 565,933"/>
    <rect class="kraft" x="215" y="935" width="350" height="355"/>
    <polygon class="kraft" points="215,935 65,905 50,965 65,1315 90,1325 215,1290"/>
    <polygon class="kraft" points="565,935 715,905 730,965 715,1315 690,1325 565,1290"/>
    <polygon class="kraft" points="100,1320 215,1290 565,1290 680,1320 690,1400 655,1415 575,1415 390,1350 205,1415 125,1415 100,1400"/>
  </g>

  <!-- ========== MEDIUM BOX ========== -->
  <g class="medium-box-dieline">
    <polygon class="kraft" points="928,22 1393,22 1380,40 1383,85 1373,222 948,222 938,85 940,38"/>
    <path class="kraft" d="M940,88 L845,68 Q818,110 822,160 Q828,205 860,212 L948,222 Z"/>
    <path class="kraft" d="M1380,88 L1478,68 Q1505,110 1500,160 Q1494,205 1462,212 L1373,222 Z"/>

    <path class="ink" d="M948,222 L798,202 Q787,202 788,215 L795,658 Q797,670 810,670 L855,680 L948,650 Z"/>
    <path class="ink" d="M1373,222 L1523,202 Q1536,202 1535,215 L1528,658 Q1526,670 1513,670 L1468,680 L1373,650 Z"/>
    <rect class="kraft" x="948" y="222" width="425" height="428"/>

    <g class="band-ink">
      <rect x="1265" y="22" width="7" height="628"/><rect x="1285" y="22" width="7" height="628"/>
      <rect x="948" y="560" width="425" height="7"/><rect x="948" y="580" width="425" height="7"/>
    </g>
    <g class="band-kraft">
      <rect x="793" y="560" width="155" height="6"/><rect x="793" y="580" width="155" height="6"/>
      <rect x="1373" y="560" width="157" height="6"/><rect x="1373" y="580" width="157" height="6"/>
    </g>

    <rect class="art-fill" x="1112" y="88" width="100" height="66" rx="26" role="img" aria-label="Burger pattern illustration"/>

    <!-- brand name -->
    <rect class="band-kraft" x="1212" y="535" width="135" height="80"/>
    <g transform="rotate(180 1279 575)">
      <text class="brand-name on-kraft" x="1279" y="570">COPPERFIELD</text>
      <text class="brand-name on-kraft" x="1279" y="598">GRILL</text>
    </g>

    <!-- burger checklist -->
    <g class="burger-checklist">
      <g transform="translate(906,520) rotate(90)"><text class="menu-item on-ink" text-anchor="end" x="0">COPPERFIELD GRILL</text></g>
      <g transform="translate(880,520) rotate(90)"><text class="menu-item on-ink" text-anchor="end">AUSSIE BURGER</text></g>
      <g transform="translate(854,520) rotate(90)"><text class="menu-item on-ink" text-anchor="end">HANGOVER BURGER</text></g>
      <g transform="translate(828,520) rotate(90)"><text class="menu-item on-ink" text-anchor="end">SPECIAL</text></g>
      <rect class="tick-box on-ink" x="906" y="530" width="10" height="10" rx="2"/>
      <rect class="tick-box on-ink" x="880" y="530" width="10" height="10" rx="2"/>
      <rect class="tick-box on-ink" x="854" y="530" width="10" height="10" rx="2"/>
      <rect class="tick-box on-ink" x="828" y="530" width="10" height="10" rx="2"/>
    </g>

    <!-- slogan -->
    <g transform="rotate(180 1090 390)">
      <text class="slogan medium-box" x="990" y="305">GRIDDLE,</text>
      <text class="slogan medium-box" x="990" y="358">SIZZLE,</text>
      <text class="slogan medium-box" x="990" y="412">JUICY</text>
      <text class="slogan medium-box" x="990" y="466">PATTY</text>
      <text class="slogan medium-box" x="990" y="522">GIVER</text>
    </g>

    <!-- back and base -->
    <polygon class="ink" points="948,650 1373,650 1385,795 935,795"/>
    <polygon class="kraft" points="948,652 848,730 935,792"/>
    <polygon class="kraft" points="1373,652 1473,730 1385,792"/>
    <polygon class="ink" points="935,795 1385,795 1378,935 943,935"/>
    <polygon class="kraft" points="935,797 848,853 943,933"/>
    <polygon class="kraft" points="1385,797 1473,853 1378,933"/>
    <rect class="kraft" x="943" y="935" width="435" height="440"/>
    <polygon class="kraft" points="943,935 795,905 778,965 795,1400 820,1410 943,1375"/>
    <polygon class="kraft" points="1378,935 1528,905 1545,965 1528,1400 1503,1410 1378,1375"/>
    <polygon class="kraft" points="830,1405 943,1375 943,1500 855,1500 835,1485"/>
    <polygon class="kraft" points="1378,1375 1490,1405 1485,1485 1465,1500 1378,1500"/>
    <polygon class="ink" points="943,1375 1378,1375 1385,1500 1160,1438 935,1500"/>
  </g>
</svg>
</body>
</html>
```